Business Card Design

We are a commercial real estate brokerage in San Francisco, leasing office buildings downtown.
I would like a clean, elegant look. Simple but powerful .

Industry/Entity Type

Business

Contact Information for Business Card

Colin Farrow
lic# 07281549
415.555.0172
colin@tarvo-commercial.example
tarvo-commercial.example

```html
<!DOCTYPE html>
<html lang="en">
<head>
<meta charset="utf-8">
<title>Tarvo Commercial – Business Card</title>
<link href="https://fonts.googleapis.com/css2?family=Questrial&display=swap" rel="stylesheet">
<style>
  :root {
    --page: #ffffff;
    --side-panel: #4a4a4a;
    --card-dark: #2a2a2a;
    --logo-light: #b4c0d4;
    --logo-mid: #8c9bb6;
    --logo-dark: #5d6c88;
    --accent: #7d8bab;
    --icon-bg: #8593b0;
    --text-light: #f4f4f4;
    --fold-line: #1c1c1c;
  }
  * { margin: 0; padding: 0; box-sizing: border-box; }
  html, body {
    width: 997px;
    height: 1200px;
    overflow: hidden;
    background: var(--page);
  }
  .card {
    position: absolute;
    left: 58px;
    top: 343px;
    width: 880px;
    height: 514px;
    background: var(--card-dark);
    font-family: "Questrial", "Century Gothic", sans-serif;
    color: var(--text-light);
    overflow: hidden;
  }
  .card__side {
    position: absolute;
    left: 0; top: 0;
    width: 332px;
    height: 100%;
    background: var(--side-panel);
  }
  .logo-tab {
    position: absolute;
    left: 14px;
    top: 97px;
    width: 330px;
    height: 234px;
    background: linear-gradient(135deg, var(--logo-light) 0%, var(--logo-mid) 50%, var(--logo-dark) 100%);
    box-shadow: 0 38px 30px -18px rgba(0,0,0,0.55);
    display: flex;
    flex-direction: column;
    align-items: center;
    justify-content: flex-end;
    padding-bottom: 40px;
  }
  .logo-tab__fold {
    position: absolute;
    right: -6px;
    width: 3px;
    background: var(--fold-line);
  }
  .logo-tab__fold--top { top: -6px; height: 40px; }
  .logo-tab__fold--bottom { bottom: -6px; height: 40px; }
  .logo-tab__name {
    font-size: 44px;
    letter-spacing: 1px;
    color: var(--text-light);
    line-height: 1;
  }
  .logo-tab__sub {
    font-size: 20px;
    letter-spacing: 1px;
    color: var(--text-light);
    margin-top: 4px;
  }
  .identity {
    position: absolute;
    right: 24px;
    top: 138px;
    text-align: right;
  }
  .identity__name {
    font-size: 57px;
    line-height: 1;
    letter-spacing: 0.5px;
    color: var(--text-light);
  }
  .identity__licence {
    font-size: 32px;
    line-height: 1;
    margin-top: 6px;
    color: var(--accent);
  }
  .contact-list {
    position: absolute;
    left: 361px;
    top: 349px;
    list-style: none;
  }
  .contact-list__item {
    display: flex;
    align-items: center;
    height: 35px;
    margin-bottom: 15px;
    font-size: 28px;
    color: var(--text-light);
  }
  .contact-list__icon {
    width: 35px;
    height: 35px;
    margin-right: 12px;
    flex: none;
  }
</style>
</head>
<body>
  <section class="card">
    <div class="card__side"></div>

    <div class="logo-tab">
      <span class="logo-tab__fold logo-tab__fold--top"></span>
      <span class="logo-tab__fold logo-tab__fold--bottom"></span>
      <span class="logo-tab__name">TARVO</span>
      <span class="logo-tab__sub">COMMERCIAL</span>
    </div>

    <div class="identity">
      <h1 class="identity__name">COLIN FARROW</h1>
      <p class="identity__licence">LIC# 07281549</p>
    </div>

    <ul class="contact-list">
      <li class="contact-list__item">
        <svg class="contact-list__icon" viewBox="0 0 35 35" aria-hidden="true">
          <rect width="35" height="35" rx="3" fill="var(--icon-bg)"/>
          <rect x="7" y="16" width="21" height="11" rx="2" fill="#fff"/>
          <path d="M6 15 Q17.5 6 29 15 L26 17 L24 14 Q17.5 10 11 14 L9 17 Z" fill="#fff"/>
          <circle cx="17.5" cy="21.5" r="2.5" fill="var(--icon-bg)"/>
        </svg>
        <span>415.555.0172</span>
      </li>
      <li class="contact-list__item">
        <svg class="contact-list__icon" viewBox="0 0 35 35" aria-hidden="true">
          <rect width="35" height="35" rx="3" fill="var(--icon-bg)"/>
          <rect x="7" y="11" width="21" height="15" fill="none" stroke="#fff" stroke-width="2"/>
          <path d="M7 11 L17.5 20 L28 11" fill="none" stroke="#fff" stroke-width="2"/>
        </svg>
        <span>colin@tarvo-commercial.example</span>
      </li>
      <li class="contact-list__item">
        <svg class="contact-list__icon" viewBox="0 0 35 35" aria-hidden="true">
          <rect width="35" height="35" rx="3" fill="var(--icon-bg)"/>
          <rect x="7" y="7" width="21" height="21" fill="none" stroke="#fff" stroke-width="2"/>
          <circle cx="17.5" cy="17.5" r="4" fill="none" stroke="#fff" stroke-width="2"/>
          <path d="M21.5 14 V19.5 Q21.5 22 24 21" fill="none" stroke="#fff" stroke-width="2"/>
        </svg>
        <span>tarvo-commercial.example</span>
      </li>
    </ul>
  </section>
</body>
</html>
```